Quillby Systems Business Card

Create an appealing and elegant Business card for quillby systems. Include logo and use related colors from website, be creative. Include Business name, my name, tile, address, contacts, address, and social media contacts if possible. Logo PSD file is attached.

Bleed Area: 3.46" x 2.32"
Trim: 3.3" x 2.16"
Safe Area: 3.14" x 2.02"

Save files as vector-based PDF with outlined text and PNG.
No crop marks
CMYK color setting

Business Card Info:

Quillby Systems

Dorian Vellacott
Owner

418 Bramlow Rd Unit C
Harlow Cove, QB 02771
t. 1.888.562.3907
e. dorian.v@quillbysys.example
w. www.quillbysys.example

facebook. www.facebook.com/QuillbySys
twitter. twitter.com/quillbysys
pinterest. www.pinterest.com/quillbysys/

Target Market(s)

Business Owners and Partners

Industry/Entity Type

Business

Requirements
Must have
• Logo and related colors from website

```html
<!DOCTYPE html>
<html lang="en">
<head>
<meta charset="utf-8">
<title>Quillby Systems Business Card</title>
<link rel="stylesheet" href="https://fonts.googleapis.com/css2?family=Open+Sans:wght@400;600&family=Arimo:wght@400;700&display=swap">
<style>
  :root {
    --backdrop: #2e2e2e;
    --paper: #ffffff;
    --brand-blue: #4b75a8;
    --ink: #111111;
    --on-blue: #ffffff;
  }
  * { margin: 0; padding: 0; box-sizing: border-box; }
  html, body { width: 1000px; height: 1200px; overflow: hidden; }
  body { background: var(--backdrop); position: relative; font-family: "Arimo", Arial, sans-serif; }

  .card { position: absolute; left: 136px; width: 745px; height: 436px; background: var(--paper); overflow: hidden; }
  .card-front { top: 115px; }
  .card-back { top: 649px; }

  .front-band { position: absolute; left: 0; right: 0; bottom: 0; height: 23px; background: var(--brand-blue); }

  .wordmark { position: absolute; font-family: "Open Sans", sans-serif; font-weight: 400; color: var(--ink); line-height: 1.05; }
  .wordmark-front { left: 0; right: 0; top: 140px; font-size: 76px; text-align: center; }
  .wordmark-back { left: 50px; width: 290px; top: 88px; font-size: 40px; text-align: left; }

  .contact-list { position: absolute; right: 50px; top: 36px; list-style: none; color: var(--brand-blue); font-size: 13.5px; }
  .contact-list li { display: flex; justify-content: flex-end; align-items: center; height: 26px; }
  .icon { width: 18px; height: 18px; margin-left: 10px; flex: none; }

  .address { position: absolute; right: 91px; top: 140px; color: var(--brand-blue); font-size: 13.5px; line-height: 22px; text-align: right; font-style: normal; }

  .back-panel { position: absolute; left: 0; right: 0; top: 256px; bottom: 0; background: var(--brand-blue); color: var(--on-blue); }
  .person { position: absolute; right: 447px; top: 58px; text-align: right; }
  .person-name { font-size: 20px; font-weight: 400; }
  .person-name strong { font-weight: 700; }
  .person-title { font-size: 15px; margin-top: 4px; }

  .social-list { position: absolute; right: 50px; top: 53px; list-style: none; font-size: 13.5px; }
  .social-list li { display: flex; justify-content: flex-end; align-items: center; height: 29px; }
</style>
</head>
<body>

<section class="card card-front" aria-label="Card front">
  <div class="wordmark wordmark-front">Quillby Systems</div>
  <div class="front-band"></div>
</section>

<section class="card card-back" aria-label="Card back">
  <div class="wordmark wordmark-back">Quillby<br>Systems</div>

  <ul class="contact-list">
    <li>1.888.562.3907
      <svg class="icon" viewBox="0 0 18 18" fill="none" stroke="currentColor" stroke-width="1.2"><circle cx="9" cy="9" r="8"/><path d="M6 5c-1 1-1 3 1 5s4 2 5 1l-1.5-1.5-1 .8c-.8-.3-1.6-1.1-1.9-1.9l.8-1L6 5z"/></svg>
    </li>
    <li>dorian.v@quillbysys.example
      <svg class="icon" viewBox="0 0 18 18" fill="none" stroke="currentColor" stroke-width="1.2"><circle cx="9" cy="9" r="8"/><circle cx="9" cy="9" r="2"/><path d="M11 7v3c0 1 2 1 2-1a4 4 0 1 0-2 3.4"/></svg>
    </li>
    <li>www.quillbysys.example
      <svg class="icon" viewBox="0 0 18 18" fill="none" stroke="currentColor" stroke-width="1.2"><circle cx="9" cy="9" r="7"/><ellipse cx="9" cy="9" rx="3" ry="7"/><path d="M2 9h14M3.5 5.5h11M3.5 12.5h11"/></svg>
    </li>
  </ul>

  <address class="address">418 Bramlow Rd Unit C<br>Harlow Cove, QB 02771</address>

  <div class="back-panel">
    <div class="person">
      <p class="person-name"><strong>Dorian</strong> Vellacott</p>
      <p class="person-title">Owner</p>
    </div>
    <ul class="social-list">
      <li>www.friendlink.example/QuillbySys
        <svg class="icon" viewBox="0 0 18 18" fill="none" stroke="currentColor" stroke-width="1.2"><circle cx="9" cy="9" r="8"/></svg>
      </li>
      <li>chirpline.example/quillbysys
        <svg class="icon" viewBox="0 0 18 18" fill="none" stroke="currentColor" stroke-width="1.2"><circle cx="9" cy="9" r="8"/></svg>
      </li>
      <li>www.pinboard.example/quillbysys/
        <svg class="icon" viewBox="0 0 18 18" fill="none" stroke="currentColor" stroke-width="1.2"><circle cx="9" cy="9" r="8"/></svg>
      </li>
    </ul>
  </div>
</section>

</body>
</html>
```